QDV Construction and Remodeling

Prefer a matte black card with some colors that pop, but subtle. Contact info. Show General Contractor professional way. Can you please remove renovations repairs maintenance off of my logo.

Target Market(s)

Property and business investors. Homeowners

Industry/Entity Type

Construction

Contact Information for Business Card

Name: Dorian Falkner, Title: CEO, Phone: 555-216-0394, Email: Dorian@QDVbuildTrx.com, website: www QDVbuildTrx.com

Font styles to use
Other font styles liked:
• Designer choose

Colors

Designer to choose colors to be used in the design.

Requirements
Must have
• Uniqueness. Double sided since it wont let me choose that. Professional look, be eye catching and catchy. QR code to my website
Nice to have
• Matte black background, subtle bright colors that pop, but I am open to anything. I also like black and gold with some red. Possible Harborton Ironclad logo colored stars somewhere around the logo or on the back. Just to rep my city
Should not have
• pink. Something you would see somewhere else. gif pictures or generated pictures.

```html
<!DOCTYPE html>
<html lang="en">
<head>
<meta charset="UTF-8">
<title>QDV Construction and Remodeling – Business Card</title>
<link href="https://fonts.googleapis.com/css2?family=Bebas+Neue&family=Lato:wght@400&display=swap" rel="stylesheet">
<style>
  :root {
    --page: #ffffff;
    --card-black: #0b0b0b;
    --red-bright: #ed1c24;
    --red-deep: #a81c23;
    --gold-light: #f3e3cc;
    --gold: #c9a07a;
    --cream: #efe3d2;
    --white: #ffffff;
  }
  html, body {
    margin: 0;
    padding: 0;
    width: 1200px;
    height: 1200px;
    overflow: hidden;
    background: var(--page);
  }
  .canvas {
    position: relative;
    width: 1200px;
    height: 1200px;
  }
  .card {
    position: absolute;
    width: 831px;
    height: 478px;
    background: var(--card-black);
    box-shadow: 0 1px 4px rgba(0,0,0,0.25);
    overflow: hidden;
  }
  .card--front { left: 189px; top: 91px; width: 829px; }
  .card--back { left: 187px; top: 639px; width: 834px; }
  .card__band {
    position: absolute;
    left: 0;
    right: 0;
    height: 26px;
    background: linear-gradient(90deg,
      var(--red-bright) 0%, var(--red-deep) 18%, var(--red-bright) 32%,
      var(--red-deep) 42%, var(--red-bright) 55%, var(--red-bright) 62%,
      var(--red-deep) 76%, var(--red-bright) 88%, var(--red-deep) 100%);
  }
  .card__band--top { top: 0; }
  .card__band--bottom { bottom: 0; }

  .identity {
    position: absolute;
    right: 465px;
    top: 188px;
    text-align: right;
  }
  .identity__name {
    margin: 0;
    font-family: 'Bebas Neue', sans-serif;
    font-size: 60px;
    line-height: 1;
    letter-spacing: 0.5px;
    color: var(--gold-light);
    background: linear-gradient(90deg, var(--gold-light) 0%, var(--gold) 45%, var(--gold-light) 75%, var(--gold-light) 100%);
    -webkit-background-clip: text;
    background-clip: text;
    -webkit-text-fill-color: transparent;
  }
  .identity__title {
    margin: 4px 0 0;
    font-family: 'Lato', sans-serif;
    font-size: 21px;
    color: var(--cream);
  }
  .divider {
    position: absolute;
    left: 413px;
    top: 200px;
    width: 3px;
    height: 79px;
    background: var(--red-bright);
  }
  .contact {
    position: absolute;
    left: 449px;
    top: 196px;
    margin: 0;
    padding: 0;
    list-style: none;
    font-family: 'Lato', sans-serif;
    font-size: 20px;
    color: var(--cream);
  }
  .contact__item {
    display: flex;
    align-items: center;
    height: 30px;
  }
  .contact__icon {
    width: 20px;
    height: 20px;
    margin-right: 13px;
    flex: none;
  }
  .contact__item--phone { color: var(--gold); }

  .brand {
    position: absolute;
    left: 0;
    right: 0;
    top: 140px;
    display: flex;
    align-items: center;
    justify-content: center;
    gap: 22px;
  }
  .brand__mark {
    width: 26px;
    height: 26px;
    background: var(--red-bright);
  }
  .brand__name {
    margin: 0;
    font-family: 'Bebas Neue', sans-serif;
    color: var(--white);
    line-height: 0.95;
    text-align: left;
  }
  .brand__initials { display: block; font-size: 118px; letter-spacing: 2px; }
  .brand__tagline { display: block; font-size: 36px; letter-spacing: 3px; }
</style>
</head>
<body>
<main class="canvas">
  <section class="card card--front" aria-label="Business card front">
    <div class="card__band card__band--top"></div>
    <div class="identity">
      <h1 class="identity__name">Dorian Falkner</h1>
      <p class="identity__title">CEO</p>
    </div>
    <div class="divider"></div>
    <ul class="contact">
      <li class="contact__item contact__item--phone">
        <svg class="contact__icon" viewBox="0 0 24 24" aria-hidden="true"><path fill="#c9a07a" d="M6.6 2.5c.6-.4 1.3-.2 1.7.4l2 3.2c.4.6.2 1.3-.3 1.7l-1.5 1.1c.9 2.2 2.5 4 4.6 5.2l1.2-1.4c.4-.5 1.2-.6 1.7-.2l3.1 2.1c.6.4.7 1.2.3 1.7l-1.4 2c-.6.8-1.6 1.2-2.6.9C9.5 17.3 5 12.6 3.5 6.6c-.2-1 .2-2 1-2.6z"/></svg>
        555-216-0394
      </li>
      <li class="contact__item">
        <svg class="contact__icon" viewBox="0 0 24 24" aria-hidden="true"><rect x="2" y="5" width="20" height="14" fill="#efe3d2"/><path d="M2 5l10 8 10-8M2 19l8-7M22 19l-8-7" stroke="#0b0b0b" stroke-width="1.6" fill="none"/></svg>
        Dorian@QDVbuildTrx.com
      </li>
      <li class="contact__item">
        <svg class="contact__icon" viewBox="0 0 24 24" aria-hidden="true"><g fill="none" stroke="#c9a07a" stroke-width="1.5"><circle cx="12" cy="12" r="10"/><ellipse cx="12" cy="12" rx="4.5" ry="10"/><path d="M2 12h20M4 7h16M4 17h16M12 2v20"/></g></svg>
        www QDVbuildTrx.com
      </li>
    </ul>
    <div class="card__band card__band--bottom"></div>
  </section>

  <section class="card card--back" aria-label="Business card back">
    <div class="card__band card__band--top"></div>
    <div class="brand">
      <span class="brand__mark" aria-hidden="true"></span>
      <h2 class="brand__name">
        <span class="brand__initials">QDV</span>
        <span class="brand__tagline">Construction &amp; Remodeling</span>
      </h2>
    </div>
    <div class="card__band card__band--bottom"></div>
  </section>
</main>
</body>
</html>
```